Night Guard Packaging

We have designed a sleek night guard for Bruxism (grinding and clenching) and would like a simple design for the front of the box.
We like simple and clean design, so maybe your artist can draw a clean image of the guard instead of using a photo?

Colours:
Our box will be Matt black, similar to example attached.
We are thinking white/black with a hint of green (the same green as the guard, also attached). The “mock-up” box artist design is the one we are leaning towards (the other examples are to give you a feel for what we like). But, if it’s too elegant it won’t feel “medical”.

The logo will need to be inverted, as it is for a white background (original attached)

Words:
Lumora Night Guard (main heading)
For Grinding & Clenching (sun heading below in smaller font).

We like, symmetry, sleek, clean, elegant, luxurious.

Maybe you artist could draw a clean image of the guard instead of using a photo? I screen shot some images with font and artists impressions. But, the customer will need to be able to see/understand the product, from the minimal details on the front of the box, as they won’t be able to open it.

```html
<!DOCTYPE html>
<html lang="en">
<head>
<meta charset="utf-8">
<title>Lumora Night Guard – Box Fronts</title>
<link href="https://fonts.googleapis.com/css2?family=Tinos&display=swap" rel="stylesheet">
<style>
  :root {
    --matt-black: #2a2828;
    --paper: #ffffff;
    --ink: #1f1d1d;
    --frame: #cfcfcf;
    --stripe-light: #ffffff;
    --stripe-dark: #231f20;
  }
  * { box-sizing: border-box; margin: 0; padding: 0; }
  html, body {
    width: 1200px; height: 1200px; overflow: hidden;
    background: var(--paper);
    font-family: "Tinos", "Times New Roman", serif;
  }
  .canvas { position: relative; width: 1200px; height: 1200px; }

  .box-front {
    position: absolute; top: 238px; width: 520px; height: 722px;
  }
  .box-front--dark { left: 64px; background: var(--matt-black); color: var(--paper); }
  .box-front--light { left: 617px; background: var(--paper); color: var(--ink); border: 1px solid var(--frame); }

  .centered { position: absolute; transform: translate(-50%, -50%); white-space: nowrap; }

  .arched-title { position: absolute; left: 0; top: 0; width: 520px; height: 420px; }
  .arched-title text { font-family: "Tinos", "Times New Roman", serif; font-size: 52px; fill: var(--paper); }

  .guard-illustration { position: absolute; border-radius: 40px 60px 30px 50px; }
  .box-front--dark .guard-illustration {
    left: 108px; top: 230px; width: 356px; height: 186px;
    background: linear-gradient(160deg, #4a4848 0%, #3a3838 60%, #333131 100%);
  }
  .box-front--light .guard-illustration {
    left: 79px; top: 290px; width: 380px; height: 260px;
    background: linear-gradient(160deg, #eeeeee 0%, #e2e2e2 60%, #d8d8d8 100%);
  }

  .subtitle--dark { left: 260px; top: 440px; font-size: 29px; }
  .title--light { left: 260px; top: 576px; font-size: 41px; }
  .subtitle--light { left: 260px; top: 620px; font-size: 22px; }

  .stripe { position: absolute; height: 5px; }
  .box-front--dark .stripe { background: var(--stripe-light); }
  .box-front--light .stripe { background: var(--stripe-dark); }

  .brand-seal {
    position: absolute; border-radius: 50%; transform: translate(-50%, -50%);
    display: flex; align-items: center; justify-content: center;
    font-size: 20px; letter-spacing: 4px;
  }
  .box-front--dark .brand-seal { left: 264px; top: 586px; width: 120px; height: 120px; border: 1.5px solid var(--paper); }
  .box-front--light .brand-seal { left: 255px; top: 170px; width: 152px; height: 152px; border: 1.5px solid var(--ink); font-size: 22px; }
</style>
</head>
<body>
<div class="canvas">

  <section class="box-front box-front--dark">
    <svg class="arched-title" viewBox="0 0 520 420" aria-label="Lumora Night Guard">
      <defs>
        <path id="title-arc" d="M 6 392 A 254 254 0 0 1 514 392"/>
      </defs>
      <text><textPath href="#title-arc" startOffset="50%" text-anchor="middle">Lumora Night Guard</textPath></text>
    </svg>
    <div class="guard-illustration" role="img" aria-label="White line drawing of the night guard mouthpiece"></div>
    <p class="centered subtitle--dark">For Grinding &amp; Clenching</p>

    <div class="stripe" style="left:0;width:146px;top:560px"></div>
    <div class="stripe" style="left:0;width:146px;top:577px"></div>
    <div class="stripe" style="left:0;width:146px;top:594px"></div>
    <div class="stripe" style="left:350px;width:170px;top:560px"></div>
    <div class="stripe" style="left:350px;width:170px;top:577px"></div>
    <div class="stripe" style="left:350px;width:170px;top:594px"></div>
    <div class="brand-seal">DENTIVA</div>
  </section>

  <section class="box-front box-front--light">
    <div class="stripe" style="left:1px;width:146px;top:142px"></div>
    <div class="stripe" style="left:1px;width:146px;top:158px"></div>
    <div class="stripe" style="left:1px;width:146px;top:177px"></div>
    <div class="stripe" style="left:351px;width:168px;top:142px"></div>
    <div class="stripe" style="left:351px;width:168px;top:158px"></div>
    <div class="stripe" style="left:351px;width:168px;top:177px"></div>
    <div class="brand-seal">DENTIVA</div>

    <div class="guard-illustration" role="img" aria-label="Black line drawing of the night guard mouthpiece"></div>
    <h1 class="centered title--light" style="font-weight:400">Lumora Night Guard</h1>
    <p class="centered subtitle--light">For Grinding &amp; Clenching</p>
  </section>

</div>
</body>
</html>
```